Awesome Design for a Stillwater Therapy

We need a simple but modern design for a Stillwater Therapy which opened recently. A logo, letterhead and a business card. Maybe something with the greek letter psi.

Font styles to use
Serif
Sans Serif

```html
<!DOCTYPE html>
<html lang="en">
<head>
<meta charset="utf-8">
<title>Stillwater Therapy – Stationery</title>
<link href="https://fonts.googleapis.com/css2?family=Questrial&family=Poppins:wght@600&display=swap" rel="stylesheet">
<style>
  :root{
    --backdrop:#bcbdc0;
    --paper:#ffffff;
    --brand-blue:#62c2ec;
    --brand-gray:#939598;
    --ink:#8a8c8f;
    --ink-dark:#7d7f82;
  }
  *{margin:0;padding:0;box-sizing:border-box}
  html,body{width:1057px;height:1200px;overflow:hidden;background:var(--backdrop)}
  body{position:relative;font-family:"Questrial",sans-serif;color:var(--ink)}
  .letterhead{position:absolute;left:190px;top:120px;width:741px;height:959px;box-shadow:6px 6px 8px rgba(0,0,0,.25)}
  .letterhead-shapes{position:absolute;inset:0}
  .brand{position:absolute;display:flex;align-items:center;color:var(--ink)}
  .brand-mark{border-radius:50%;background:var(--ink);flex:none}
  .brand-name{line-height:1;font-family:"Questrial",sans-serif}
  .brand-name .line1{display:block;letter-spacing:.04em}
  .brand-name .line2{display:block}
  .letterhead .brand{left:200px;top:72px;gap:14px}
  .letterhead .brand-mark{width:56px;height:56px}
  .letterhead .brand-name .line1{font-size:31px}
  .letterhead .brand-name .line2{font-size:33px;margin-top:4px}
  .contact-grid{position:absolute;left:81px;top:827px;width:640px;height:78px}
  .contact-item{position:absolute;display:flex;align-items:center;gap:10px;font-size:16px;color:var(--ink);line-height:1.15}
  .contact-icon{width:38px;height:33px;background:var(--brand-blue);display:flex;align-items:center;justify-content:center;flex:none}
  .contact-icon svg{width:22px;height:22px;fill:var(--brand-gray)}
  .business-card{position:absolute;left:86px;top:476px;width:305px;height:174px;background:var(--paper);box-shadow:5px 5px 7px rgba(0,0,0,.3);overflow:hidden}
  .card-topbar{position:absolute;left:54px;top:0;width:197px;height:5px;background:var(--brand-blue);border-radius:0 0 4px 4px}
  .card-bottom-blue{position:absolute;left:0;bottom:0;width:117px;height:11px;background:var(--brand-blue);border-radius:0 0 6px 0}
  .card-bottom-gray{position:absolute;left:119px;bottom:0;right:0;height:4px;background:var(--brand-gray);border-radius:4px 0 0 0}
  .business-card .brand{left:62px;top:18px;gap:8px}
  .business-card .brand-mark{width:28px;height:28px}
  .business-card .brand-name .line1{font-size:15px}
  .business-card .brand-name .line2{font-size:16px;margin-top:2px}
  .card-person{position:absolute;right:186px;top:106px;text-align:right}
  .card-person .name{font-family:"Poppins",sans-serif;font-weight:600;font-size:15px;color:var(--ink-dark);line-height:1.1}
  .card-person .role{font-size:12px;color:var(--ink);line-height:1.1}
  .card-divider{position:absolute;left:152px;top:84px;width:1px;height:73px;background:var(--ink)}
  .card-contacts{position:absolute;left:158px;top:91px;list-style:none}
  .card-contacts li{display:flex;align-items:center;gap:6px;font-size:7px;line-height:1.25;height:13.5px}
  .card-contacts li.address{height:20px;margin-top:1px}
  .card-contacts svg{width:11px;height:11px;fill:var(--ink);flex:none}
</style>
</head>
<body>
<svg width="0" height="0" style="position:absolute" aria-hidden="true">
  <defs>
    <symbol id="icon-phone" viewBox="0 0 24 24"><path d="M6.6 2.5 9.3 6c.4.5.3 1.2-.1 1.6L7.6 9.1c1.3 2.8 4.4 5.9 7.3 7.3l1.5-1.6c.4-.4 1.1-.5 1.6-.1l3.5 2.7c.5.4.6 1.1.2 1.6l-1.6 2c-.6.7-1.6 1-2.5.7C10.7 19.4 4.6 13.3 2.3 6.4c-.3-.9 0-1.9.7-2.5l2-1.6c.5-.4 1.2-.3 1.6.2z"/></symbol>
    <symbol id="icon-mail" viewBox="0 0 24 24"><path d="M2 5h20v14H2zm2 2v.4l8 5.6 8-5.6V7zm0 2.8V17h5.2zm16 0L14.8 17H20zM10.8 14.2 5.9 17h12.2l-4.9-2.8-1.2.9z"/></symbol>
    <symbol id="icon-globe" viewBox="0 0 24 24"><path d="M12 2a10 10 0 1 0 0 20 10 10 0 0 0 0-20zm-1 2.1V8H7.6c.7-2 1.9-3.5 3.4-3.9zm2 0c1.5.4 2.7 1.9 3.4 3.9H13zM5.9 7.1A8 8 0 0 1 8 5a10 10 0 0 0-1.4 3H4.8a8 8 0 0 1 1.1-.9zM4.1 10h2.1a15 15 0 0 0 0 4H4.1a8 8 0 0 1 0-4zm4.1 0H11v4H8.2a13 13 0 0 1 0-4zm4.8 0h2.8a13 13 0 0 1 0 4H13zm4.8 0h2.1a8 8 0 0 1 0 4h-2.1a15 15 0 0 0 0-4zm-13 6h1.8A10 10 0 0 0 8 19a8 8 0 0 1-3.2-3zm2.8 0H11v3.9c-1.5-.4-2.7-1.9-3.4-3.9zm5.4 0h3.4c-.7 2-1.9 3.5-3.4 3.9zm4.4 0h1.8A8 8 0 0 1 16 19a10 10 0 0 0 1.4-3zm0-8A10 10 0 0 0 16 5a8 8 0 0 1 3.2 3z"/></symbol>
    <symbol id="icon-pin" viewBox="0 0 24 24"><path d="M12 1.5a7.5 7.5 0 0 0-7.5 7.5c0 5.6 7.5 13.5 7.5 13.5s7.5-7.9 7.5-13.5A7.5 7.5 0 0 0 12 1.5zm0 10.5a3 3 0 1 1 0-6 3 3 0 0 1 0 6z"/></symbol>
  </defs>
</svg>

<section class="letterhead" aria-label="Letterhead">
  <svg class="letterhead-shapes" viewBox="0 0 741 959" width="741" height="959" aria-hidden="true">
    <rect width="741" height="959" fill="var(--paper)"/>
    <path d="M0 0H741V339A49 49 0 0 1 692 290V59L673 43H0Z" fill="var(--brand-blue)"/>
    <path d="M0 959H741V916H68L49 899V669A49 49 0 0 0 0 620Z" fill="var(--brand-gray)"/>
  </svg>

  <div class="brand">
    <span class="brand-mark"></span>
    <span class="brand-name"><span class="line1">STILLWATER</span><span class="line2">Therapy</span></span>
  </div>

  <div class="contact-grid">
    <div class="contact-item" style="left:0;top:0"><span class="contact-icon"><svg><use href="#icon-phone"/></svg></span>(+44)7700 900123</div>
    <div class="contact-item" style="left:0;top:44px"><span class="contact-icon"><svg><use href="#icon-mail"/></svg></span>hello@stillwatertherapy.com</div>
    <div class="contact-item" style="left:334px;top:0"><span class="contact-icon"><svg><use href="#icon-globe"/></svg></span>www.stillwatertherapy.com</div>
    <div class="contact-item" style="left:334px;top:44px"><span class="contact-icon"><svg><use href="#icon-pin"/></svg></span><span>214 Harbor Lane<br>Fairview, VA 23401</span></div>
  </div>
</section>

<section class="business-card" aria-label="Business card">
  <div class="card-topbar"></div>
  <div class="brand">
    <span class="brand-mark"></span>
    <span class="brand-name"><span class="line1">STILLWATER</span><span class="line2">Therapy</span></span>
  </div>
  <div class="card-person">
    <div class="name">Your Name</div>
    <div class="role">President</div>
  </div>
  <div class="card-divider"></div>
  <ul class="card-contacts">
    <li><svg><use href="#icon-phone"/></svg>(+44)7700 900123</li>
    <li><svg><use href="#icon-mail"/></svg>hello@stillwatertherapy.com</li>
    <li><svg><use href="#icon-globe"/></svg>www.stillwatertherapy.com</li>
    <li class="address"><svg><use href="#icon-pin"/></svg><span>214 Harbor Lane<br>Fairview, VA 23401</span></li>
  </ul>
  <div class="card-bottom-blue"></div>
  <div class="card-bottom-gray"></div>
</section>
</body>
</html>
```